Wander Pose Journeys Postcard Design

We need a promotional CMYK postcard that we will leave at yoga studios to advertise our yoga holidays to Cambodia.

Filecrate link with possible photos + logos (please see photo notes below): https://www.filecrate.net/sh/4kqpw81xz3m5v9a/BBLmtyyq0K3Pz7RVbnGhQeLu?dl=0

Please message me if you need more info or have issues with the photos.

Thanks

Target Market(s)

Brand style:
High quality and discerning, healthy and ethically aware, natural, unique and boutique, a sense of exploration, pitched at busy professionals and high end consumers. (not hippy!)

Industry/Entity Type

Travel

Font styles to use
Serif
Sans Serif

Colors
abd036
0492cd

Requirements
Must have
• CMYK
• *I have attached a file crate link to various named pictures that you may use for your design selection but you are free to supply other royalty free pictures if you wish. There are a number of choices and we do not expect all of these to be used - just offering a selection so hopefully some will be suitable for your design. Here is the filecrate link: https://www.filecrate.net/sh/4kqpw81xz3m5v9a/BBLmtyyq0K3Pz7RVbnGhQeLu?dl=0
• *Main front Picture must be one associated with Cambodia. Expecting several smaller photos on front as well
• *Must have at least one of our yoga photos on it.
• *The reverse side must have some white space around the address area so people could write a few lines and send as a postcard.
• *Please use the logo colours (lime and turquoise) with black or white as the main theme/colours.
• *Thinking to have a main photo of Cambodia on front with smaller photos and the 7 words featured (see text below).
• Text to include
• Front of postcard:
• (WPJ logo - prefer the coloured logo but needs to look ok with rest of photo - so can have white or black background or I have it in black & white - have attached coloured but message me if you wish for all B&W logo)
• Wander Pose Journeys
• Wander, never settle!
• 7 night Grand Asana Getaway Bundle.
• Siem Reap, Cambodia
• Discover
• Relax
• Cuisine
• Culture
• Yoga
• Boutique
• Ethical travel
• Reverse of postcard:
• Boutique, Unique, Fantastique!
• Do you need a high quality cultural holiday that explores, experiences, delights, relaxes, indulges - and has daily yoga? Are you short of time to do your holiday planning but still want some choices. Do you prefer a holiday over a strict yoga retreat? Do you want to use an ethical travel company to ensure your vacation does some good for others as well?
• Then visit:
• wanderposejourneys.com
• for dates and details.
• (also needs a box that I can stamp different codes into - must have white background - stamp text height is 4mm and max width is 27mm - needs the following text in or around the box)
• Special Promotion Code:
• Use this code with booking to receive a $200 AUD Movaleta ecard
Nice to have
• Printers Specification (please see Printlane.com.au for other specifications if needed)
• Acceptable File Formats:
• We support a variety of file formats for uploaded designs.
• Adobe Acrobat 9 Document (*.pdf) (recommended)
• JPEG Image (*.jpg,*.jpeg)
• A6 postcard size:
• Full Bleed Size
• 151 x 108 mm
• 1783 x 1275 pixels
• Document Trim Size
• 148 x 105 mm
• 1748 x 1240 pixels
• CMYK
• Digital Imaging
• You may create printed products on our web site using digitized images from a variety of sources. Your designs, photos and images can come from a digital camera, scanner, or the Web.
• Any image you plan to use must be saved at approximately 300-dpi at 100% output size for the very best printing results. It’s helpful to know that shrinking an image on a product will increase its resolution. For example, an image captured at 600 x 900 pixels has 150-dpi at 4” x 6”. Howver, it can be printed at 300-dpi by reducing its dimensions on the product to 2” x 3”.
• Images from a Digital Camera
• If you wish to use images from a digital camera, before you snap pictures make sure the camera is set at a high enough resolution to result in 300 DPI at the intended photo print size. Most cameras have various settings for resolutions. The highest resolution for your camera depends on how many megapixels it has.
• You cannot increase the resolution of a photo after it is taken, except by reducing its printed dimensions (after you upload the image). Be careful when cropping a photo after it is taken. Cropping will reduce the number of pixels in the final image.
• Images from a Scanner
• Like a digital camera, a scanner must be preset to the proper resolution before image capture. Many scanners default to 150-dpi (or spi). Set your scanner’s resolution so that it results in 300-dpi at the image’s final print size. If your resulting scanned image is smaller than the recommended size or has less dpi than you need, you should either rescan your original at a higher resolution, or use the image for a smaller printed area.
• Images from the Web
• Images found on the web are typically at a resolution of 72-dpi. This resolution is much too low for quality printing. In addition, most images on the web are protected by copyright laws. For these reasons, we do not recommend using images from the web.
Should not have
• Hippy elements

```html
<!DOCTYPE html>
<html lang="en">
<head>
<meta charset="utf-8">
<title>Wander Pose Journeys – Postcard</title>
<link rel="stylesheet" href="https://fonts.googleapis.com/css2?family=Niconne&family=Roboto+Condensed:wght@400;700&family=Roboto:wght@300;400&display=swap">
<style>
:root{
  --turquoise:#0492cd;
  --sky:#2aa9dc;
  --pale-sky:#bfe5f4;
  --lime:#abd036;
  --blush:#e6c6dc;
  --ink:#5a5f66;
  --rule:#6b6b6b;
  --paper:#ffffff;
  --backdrop:#eef1f3;
}
*{box-sizing:border-box;margin:0;padding:0}
html,body{width:941px;height:1200px;overflow:hidden}
body{background:var(--backdrop);position:relative;font-family:"Roboto",Arial,sans-serif}

.postcard{position:absolute;left:80px;width:780px;height:553px;background:var(--paper);overflow:hidden;box-shadow:0 3px 10px rgba(0,0,0,.18)}
.postcard--front{top:32px;background:linear-gradient(160deg,#eaf2fa 0%,#f6f4fb 45%,#fbf6fa 100%)}
.postcard--back{top:615px}

/* front */
.hero-photo{position:absolute;left:0;top:0;width:450px;height:553px;
  background:linear-gradient(180deg,#b9cfee 0%,#d9cdea 35%,var(--blush) 60%,#b690d6 100%);
  -webkit-mask-image:linear-gradient(90deg,#000 78%,transparent 100%);mask-image:linear-gradient(90deg,#000 78%,transparent 100%)}
.brand-script{position:absolute;left:30px;font-family:"Niconne",cursive;color:var(--sky);line-height:1;white-space:nowrap}
.brand-script--title{top:26px;font-size:32px}
.brand-script--tagline{top:62px;font-size:28px}

.circle-photo{position:absolute;width:136px;height:136px;border-radius:50%;border:6px solid var(--sky);box-shadow:0 2px 6px rgba(0,0,0,.25)}
.circle-photo--monk{left:332px;top:52px;background:radial-gradient(circle at 50% 55%,#c2402c,#5a3424 70%)}
.circle-photo--statue{left:332px;top:208px;background:radial-gradient(circle at 50% 50%,#d9c7ab,#6f8a58 75%)}
.circle-photo--spa{left:332px;top:364px;background:radial-gradient(circle at 50% 50%,#e9ddc6,#7a5a3c 75%)}

.offer{position:absolute;left:480px;top:34px;width:280px;text-align:center}
.offer__headline{font-family:"Roboto Condensed",Arial,sans-serif;color:var(--sky);text-transform:uppercase;font-size:23px;line-height:1.05;display:flex;align-items:center;gap:6px;justify-content:center}
.offer__nights{font-family:"Roboto Condensed",Arial,sans-serif;font-weight:700;color:var(--lime);font-size:56px;line-height:.9}
.offer__place{color:var(--lime);font-size:19px;margin-top:18px;font-weight:300}
.offer__words{list-style:none;margin-top:18px;color:var(--sky);font-size:27px;font-weight:300;line-height:1.2}
.offer__brand{position:absolute;left:480px;top:370px;width:280px;display:flex;flex-direction:column;align-items:center;gap:8px}
.brand-dot{width:46px;height:46px;border-radius:50%;background:var(--sky)}
.brand-name{font-family:"Roboto Condensed",Arial,sans-serif;font-weight:700;color:var(--lime);font-size:18px;text-transform:uppercase;letter-spacing:1px}

.swoosh{position:absolute;left:0;top:0;pointer-events:none}

/* back */
.back-photo{position:absolute;left:0;top:0;width:420px;height:553px;background:linear-gradient(180deg,#f3f7fb 0%,#eef2f6 55%,#e4e9ee 100%)}
.back-copy{position:absolute;left:28px;top:78px;width:370px}
.back-copy__heading{font-family:"Niconne",cursive;color:var(--sky);font-size:30px;text-align:right;margin-bottom:12px}
.back-copy__questions{list-style:none;color:var(--ink);font-size:13.5px;line-height:1.45}
.back-copy__questions li{position:relative;padding-left:16px;margin-bottom:4px}
.back-copy__questions li::before{content:"";position:absolute;left:2px;top:7px;width:6px;height:6px;border-radius:50%;background:var(--sky)}
.back-copy__cta{text-align:center;margin-top:14px;line-height:1.05}
.cta-lead,.cta-tail{color:var(--lime);font-size:24px;font-weight:300}
.cta-url{color:var(--turquoise);font-size:30px;font-weight:400}

.promo{position:absolute;left:22px;top:432px;width:270px;height:104px;border:2px dashed #222;background:var(--paper);display:flex;align-items:center;gap:10px;padding:8px}
.promo__photo{flex:none;width:80px;height:80px;border-radius:50%;background:radial-gradient(circle,#efe4cf,#8b6a46 80%)}
.promo__text{flex:1;text-align:center;color:var(--ink);font-size:11px;line-height:1.3}
.promo__amount{display:block;background:var(--lime);color:var(--paper);font-size:19px;margin:3px 0}
.promo__fine{font-size:7px;color:#888}

.address-side{position:absolute;left:420px;top:0;width:360px;height:553px;background:var(--paper);border-left:1px solid #e3e3e3}
.stamp-box{position:absolute;right:36px;top:40px;width:92px;height:92px;border:2px solid #222}
.address-line{position:absolute;left:40px;width:284px;height:0;border-top:1.5px solid var(--rule)}
</style>
</head>
<body>

<section class="postcard postcard--front" aria-label="Postcard front">
  <div class="hero-photo" role="img" aria-label="Yoga pose by the water at sunset"></div>

  <svg class="swoosh" width="780" height="553" viewBox="0 0 780 553" aria-hidden="true">
    <path d="M560 0 C620 30 700 20 780 60 L780 0 Z" fill="var(--pale-sky)" opacity=".8"/>
    <path d="M600 0 C660 25 720 30 780 30" stroke="var(--sky)" stroke-width="3" fill="none"/>
    <path d="M0 500 C160 460 320 535 520 505 C640 490 720 495 780 475 L780 553 L0 553 Z" fill="var(--pale-sky)" opacity=".85"/>
    <path d="M0 522 C180 480 340 548 540 518 C650 502 730 508 780 492 L780 553 L0 553 Z" fill="var(--sky)" opacity=".55"/>
    <path d="M0 490 C200 450 360 525 560 495 C660 482 730 485 780 465" stroke="var(--sky)" stroke-width="3" fill="none"/>
    <path d="M0 540 C220 505 380 550 780 505" stroke="#fff" stroke-width="2" fill="none"/>
  </svg>

  <p class="brand-script brand-script--title">Wander Pose Journeys</p>
  <p class="brand-script brand-script--tagline">Wander, never settle!</p>

  <div class="circle-photo circle-photo--monk" role="img" aria-label="Young monk holding incense"></div>
  <div class="circle-photo circle-photo--statue" role="img" aria-label="Stone Buddha statue in a garden"></div>
  <div class="circle-photo circle-photo--spa" role="img" aria-label="Spa oils and frangipani flowers"></div>

  <div class="offer">
    <h1 class="offer__headline"><span class="offer__nights">7</span><span>Night Grand Asana<br>Getaway Bundle</span></h1>
    <p class="offer__place">Siem Reap, Cambodia</p>
    <ul class="offer__words">
      <li>Discover</li><li>Relax</li><li>Cuisine</li><li>Culture</li><li>Yoga</li><li>Boutique</li><li>Ethical travel</li>
    </ul>
  </div>
  <div class="offer__brand">
    <span class="brand-dot"></span>
    <span class="brand-name">Wander Pose Journeys</span>
  </div>
</section>

<section class="postcard postcard--back" aria-label="Postcard back">
  <div class="back-photo" role="img" aria-label="Faded yoga pose on the beach"></div>

  <svg class="swoosh" width="420" height="90" viewBox="0 0 420 90" aria-hidden="true">
    <path d="M0 0 L420 0 L420 20 C320 60 180 10 0 60 Z" fill="var(--pale-sky)" opacity=".85"/>
    <path d="M0 45 C160 5 300 55 420 15" stroke="var(--sky)" stroke-width="3" fill="none"/>
    <path d="M0 70 C170 25 310 70 420 35" stroke="var(--sky)" stroke-width="1.5" fill="none" opacity=".7"/>
  </svg>

  <div class="back-copy">
    <h2 class="back-copy__heading">Boutique, Unique, Fantastique!</h2>
    <ul class="back-copy__questions">
      <li>Do you need a high quality cultural holiday that explores, experiences, delights, relaxes, indulges - and has daily yoga?</li>
      <li>Are you short of time to do your holiday planning but still want some choices.</li>
      <li>Do you prefer a holiday over a strict yoga retreat?</li>
      <li>Do you want to use an ethical travel company to ensure your vacation does some good for others as well?</li>
    </ul>
    <p class="back-copy__cta">
      <span class="cta-lead">Then visit:</span><br>
      <span class="cta-url">wanderposejourneys.com</span><br>
      <span class="cta-tail">for dates and details.</span>
    </p>
  </div>

  <div class="promo">
    <div class="promo__photo" role="img" aria-label="Spa bottles with frangipani flowers"></div>
    <p class="promo__text">Use this code with<br>booking to receive a
      <span class="promo__amount">$200 AUD</span>Movaleta<br>ECARD<br>
      <span class="promo__fine">Visit wanderposejourneys.com</span>
    </p>
  </div>

  <div class="address-side">
    <div class="stamp-box"></div>
    <span class="address-line" style="top:250px"></span>
    <span class="address-line" style="top:305px"></span>
    <span class="address-line" style="top:360px"></span>
    <span class="address-line" style="top:415px"></span>
  </div>
</section>

</body>
</html>
```